The Green Sprout Website Design

I have hosting set up through Net Harbor but need Web Design for a new company called The Green Sprout. I am a holistic health coach helping individuals and groups achieve optimum health through the elimination of processed foods, GMOs, animal foods and chemical toxins in foods, beauty and household products and the promotion of a plant focused diet. I provide education and coaching programs to ensure success. The site should include my logo, the colors of black, white, orange and green and convey a simple, natural and friendly tone. My goal is to be a friendly resource to those who want or need to transition to a vegan lifestyle but don't want to feel judged or the need to be perfect to heal and make a difference. Progress vs perfection.
Updates

The tabs would be: Home About Services Recipes Resources (Things I Love) I.e affiliate links Contact Possibly a calendar of events As for products, they would be simple ebooks or 30 day programs delivered electronically. They are still in development. I will have a link to a free book excerpt for opting into my mailing list. You can see a site I built through my school's hosting for a basic example at Lorimpelland.example While I like the basic bones of it, I wanted something more robust and not tied to the school.

```html
<!DOCTYPE html>
<html lang="en">
<head>
<meta charset="utf-8">
<title>The Green Sprout</title>
<link href="https://fonts.googleapis.com/css2?family=Montserrat:wght@400;600;700&family=Open+Sans:wght@400;600&display=swap" rel="stylesheet">
<style>
:root{
  --orange:#f7a823;
  --green:#6cbf3f;
  --green-dark:#4f9a2c;
  --black:#0d0d0d;
  --white:#ffffff;
  --ink:#222222;
  --caption:rgba(30,30,30,.72);
  --page-dark:#3b3a34;
}
*{box-sizing:border-box;margin:0;padding:0}
html,body{width:812px;height:1200px;overflow:hidden}
body{position:relative;font-family:"Open Sans",Arial,sans-serif;color:var(--white);
  background:radial-gradient(ellipse at 20% 60%,#5a6a3a 0%,transparent 45%),radial-gradient(ellipse at 85% 85%,#7a2a22 0%,transparent 40%),radial-gradient(ellipse at 80% 40%,#4d5a30 0%,transparent 45%),var(--page-dark)}
.top-band{position:absolute;left:0;top:0;width:812px;height:200px;background:var(--orange)}
.abs{position:absolute}
.header{left:124px;top:14px;width:563px;height:61px;background:var(--white)}
.brand{left:10px;top:6px;display:flex;flex-direction:column;align-items:center;width:80px}
.brand-dot{width:26px;height:26px;border-radius:50%;border:2px solid var(--orange);margin-bottom:4px}
.brand-name{font-family:"Montserrat",sans-serif;font-size:7px;color:var(--green);white-space:nowrap}
.nav{right:0;top:0;display:flex;height:61px;font-family:"Montserrat",sans-serif;font-size:10px;color:var(--ink);white-space:nowrap}
.nav a{display:flex;align-items:flex-end;padding:0 7px 10px;color:inherit;text-decoration:none}
.nav a.active{background:var(--green);color:var(--white);font-weight:600;padding:0 10px 10px}
.photo{display:block}
.hero{left:124px;top:75px;width:563px;height:285px;background:radial-gradient(ellipse at 35% 40%,#7cc244 0%,#3f8a22 35%,transparent 60%),linear-gradient(135deg,#6b4a2e,#a37a52 60%,#5a3e26)}
.hero-badge{left:497px;top:132px;width:162px;height:162px;border-radius:50%;background:var(--green);display:flex;align-items:center;justify-content:center;text-align:center;font-family:"Montserrat",sans-serif;font-weight:700;font-size:21px;line-height:1.05;box-shadow:0 4px 10px rgba(0,0,0,.25)}
.dots{left:141px;top:330px;display:flex;gap:5px}
.dots i{width:13px;height:13px;border-radius:50%;background:var(--white)}
.dots i.on{background:var(--orange)}
.welcome{left:124px;top:378px;width:374px;height:299px;background:var(--white)}
.welcome-photo{left:0;top:0;width:230px;height:205px;background:linear-gradient(120deg,#8a5a3e,#c99a78 40%,#e8d8c8 75%,#ffffff)}
.welcome-brand{left:194px;top:30px;width:80px;display:flex;flex-direction:column;align-items:center}
.welcome-title{left:193px;top:76px;font-family:"Montserrat",sans-serif;color:var(--orange);font-size:20px;font-weight:600;line-height:1;white-space:nowrap}
.welcome-sub{left:193px;top:101px;font-family:"Montserrat",sans-serif;color:var(--orange);font-size:13px;font-weight:400;white-space:nowrap}
.welcome-text{left:0;top:205px;width:343px;height:94px;background:#4a4a46;padding:11px 13px;font-size:7.6px;line-height:1.6}
.read-tab{left:343px;top:205px;width:31px;height:94px;background:var(--green);display:flex;align-items:center;justify-content:center}
.read-tab span{transform:rotate(-90deg);font-family:"Montserrat",sans-serif;font-weight:600;font-size:10px;white-space:nowrap}
.tile{overflow:hidden}
.tile .caption{position:absolute;left:0;bottom:0;width:100%;height:28px;background:var(--caption);display:flex;align-items:center;justify-content:space-between;padding:0 5px}
.tile .caption b{font-family:"Montserrat",sans-serif;font-size:8px;font-weight:600}
.tile .caption em{font-style:normal;background:var(--green);font-family:"Montserrat",sans-serif;font-size:7px;font-weight:600;padding:3px 4px}
.section-title{font-family:"Montserrat",sans-serif;color:var(--orange);font-size:10.5px;font-weight:600}
.arrows{font-family:"Montserrat",sans-serif;font-size:11px;letter-spacing:4px}
.members{left:124px;top:853px;display:grid;grid-template-columns:repeat(3,64px);grid-auto-rows:52px;gap:6px 7px}
.members div{background:linear-gradient(135deg,#cfc6b8,#8d7f6e)}
.event{left:339px;top:853px;width:157px;height:167px;background:radial-gradient(circle at 75% 45%,#b8d24a 0%,transparent 30%),radial-gradient(circle at 25% 78%,#8cc23f 0%,transparent 30%),linear-gradient(135deg,#5f8a2c,#a8b860 60%,#7a6a40)}
.event-badge{left:345px;top:862px;width:82px;height:82px;border-radius:50%;background:var(--orange);display:flex;flex-direction:column;align-items:center;justify-content:center;font-family:"Montserrat",sans-serif;line-height:1}
.event-badge small{font-size:10px}
.event-badge strong{font-size:19px;font-weight:700;margin:1px 0}
.event-badge span{font-size:10px}
.news{left:505px;top:853px;width:182px}
.news-item{display:flex;gap:8px;height:58px}
.news-item .thumb{width:64px;height:52px;flex:none;background:linear-gradient(135deg,#7a3a2a,#c8502e 45%,#5e8a2e)}
.news-item .meta{font-size:6.5px;color:var(--green);margin-top:2px}
.news-item p{font-size:8px;line-height:1.5;margin-top:1px}
.partners{left:124px;top:1040px;width:563px;height:60px;display:flex;align-items:center;justify-content:space-between;font-family:"Montserrat",sans-serif;font-weight:700;font-size:14px}
.footer{left:0;top:1117px;width:812px;height:83px;background:var(--black)}
.footer-links{left:124px;top:26px;font-size:8px;word-spacing:2px;white-space:nowrap}
.footer-links span{margin:0 7px}
.copyright{left:124px;top:46px;font-size:8px;white-space:nowrap}
.social{left:556px;top:30px;display:flex;gap:3px}
.social i{width:24px;height:24px;border-radius:50%;border:1.5px solid #2f9ad8;background:#10243a}
</style>
</head>
<body>
<div class="top-band"></div>

<header class="abs header">
  <div class="abs brand"><div class="brand-dot"></div><span class="brand-name">The Green Sprout</span></div>
  <nav class="abs nav">
    <a class="active" href="#">Home</a><a href="#">About Us</a><a href="#">Services</a><a href="#">Foods to avoid</a><a href="#">Recipes</a><a href="#">Resources</a><a href="#">Contact Us</a>
  </nav>
</header>

<div class="abs hero photo" role="img" aria-label="Bowl of fresh spinach and leafy greens on a wooden table"></div>
<div class="abs hero-badge">Progress<br>vs<br>Perfection</div>
<div class="abs dots"><i class="on"></i><i></i><i></i><i></i></div>

<section class="abs welcome">
  <div class="abs welcome-photo photo" role="img" aria-label="Smiling woman eating a fresh salad"></div>
  <div class="abs welcome-brand"><div class="brand-dot"></div><span class="brand-name">The Green Sprout</span></div>
  <h1 class="abs welcome-title">Welcome to</h1>
  <h2 class="abs welcome-sub">The Green Sprout</h2>
  <p class="abs welcome-text">Sed ut perspiciatis unde omnis iste natus error sit voluptatem accusantium doloremque laudantium, totam rem aperiam, eaque ipsa quae ab illo inventore veritatis et quasi architecto beatae vitae dicta sunt explicabo. Nemo enim ipsam voluptatem quia voluptas sit aspernatur aut odit aut fugit, sed quia consequuntur magni dolores eos qui ratione voluptatem sequi nesciunt. Neque porro quisquam est, qui dolorem ipsum quia dolor sit amet, consectetur.</p>
  <div class="abs read-tab"><span>Read More</span></div>
</section>

<div class="abs tile" style="left:505px;top:378px;width:182px;height:144px">
  <div class="photo" role="img" aria-label="Greek salad with tomato, cucumber and olives" style="width:100%;height:100%;background:linear-gradient(135deg,#c84a3a,#e8e0d0 45%,#4a7ab0)"></div>
  <div class="caption"><b>Latest Diet Foods</b><em>Read More</em></div>
</div>
<div class="abs tile" style="left:505px;top:533px;width:182px;height:144px">
  <div class="photo" role="img" aria-label="Glass of herbal drink with fresh leaves" style="width:100%;height:100%;background:linear-gradient(135deg,#d8c89a,#e8dcb0 40%,#6a9a30)"></div>
  <div class="caption"><b>Veg Drinks For Morning</b><em>Read More</em></div>
</div>
<div class="abs tile" style="left:124px;top:687px;width:181px;height:117px">
  <div class="photo" role="img" aria-label="Lettuce wrapped in a measuring tape" style="width:100%;height:100%;background:linear-gradient(135deg,#9ad050,#e8f0d0 60%,#cfe4a8)"></div>
  <div class="caption"><b>Today Diet Recipes</b><em>Read More</em></div>
</div>
<div class="abs tile" style="left:314px;top:687px;width:181px;height:117px">
  <div class="photo" role="img" aria-label="Honey dipper over a jar of honey" style="width:100%;height:100%;background:linear-gradient(135deg,#f4e8d8,#f0b060 55%,#e08a20)"></div>
  <div class="caption"><b>Honey Importance</b><em>Read More</em></div>
</div>
<div class="abs tile" style="left:505px;top:687px;width:182px;height:117px">
  <div class="photo" role="img" aria-label="Green cup of tea" style="width:100%;height:100%;background:linear-gradient(135deg,#c8e070,#8ab828 55%,#6a9a20)"></div>
  <div class="caption"><b>Green Tea</b><em>Read More</em></div>
</div>

<h3 class="abs section-title" style="left:124px;top:827px">Recent Members</h3>
<span class="abs arrows" style="left:314px;top:827px">‹ ›</span>
<h3 class="abs section-title" style="left:339px;top:827px">Recent Events</h3>
<span class="abs arrows" style="left:478px;top:827px">‹ ›</span>
<h3 class="abs section-title" style="left:504px;top:827px">Latest News</h3>
<span class="abs arrows" style="left:671px;top:827px">‹ ›</span>

<div class="abs members" role="img" aria-label="Portrait photos of nine community members">
  <div></div><div></div><div></div><div></div><div></div><div></div><div></div><div></div><div></div>
</div>

<div class="abs event photo" role="img" aria-label="Green smoothie with apples and cucumbers"></div>
<div class="abs event-badge"><small>25th June</small><strong>2014</strong><span>Diet Party</span></div>

<div class="abs news">
  <div class="news-item"><div class="thumb photo" role="img" aria-label="Chopping fresh vegetables"></div><div><div class="meta">Posted By June 30th ,14</div><p>Sed ut perspiciatis unde omnis iste natus error sit voluptatem</p></div></div>
  <div class="news-item"><div class="thumb photo" role="img" aria-label="Market stall of fresh produce"></div><div><div class="meta">Posted By June 30th ,14</div><p>Sed ut perspiciatis unde omnis iste natus error sit voluptatem</p></div></div>
  <div class="news-item"><div class="thumb photo" role="img" aria-label="Fresh strawberries"></div><div><div class="meta">Posted By June 30th ,14</div><p>Sed ut perspiciatis unde omnis iste natus error sit voluptatem</p></div></div>
</div>

<div class="abs partners">
  <span>Bramblefield</span><span>Quillon</span><span>Ferncrest</span><span>Orchardly</span><span>Seedmarrow</span>
</div>

<footer class="abs footer">
  <div class="abs footer-links">Home<span>|</span>About Us<span>|</span>Foods to avoid<span>|</span>Recipes<span>|</span>Contact Us</div>
  <div class="abs copyright">© 2014 Compnay Name, All Rights Reserved</div>
  <div class="abs social" aria-label="Social links"><i></i><i></i><i></i><i></i><i></i></div>
</footer>
</body>
</html>
```